Tidal Fern Business Cards

We need something new, fun and exciting for business cards. Our current ones are just plain and we need a design that pops. We want name, position held, phone, email on the front, and a 20% discount on the back. I have also uploaded our old business cards creative to see what we are not wanting, and how boring they were and we want something jazzed up from this, cool design and catches people attention.

```html
<!DOCTYPE html>
<html lang="en">
<head>
<meta charset="utf-8">
<title>Tidal Fern Business Card – Front 2</title>
<link rel="stylesheet" href="https://fonts.googleapis.com/css2?family=Outfit:wght@800&family=Montserrat:wght@300;400&display=swap">
<style>
  :root {
    --page: #ffffff;
    --navy: #20375a;
    --coral: #e36d69;
    --card-text: #ffffff;
    --label-text: #111111;
  }
  * { margin: 0; padding: 0; box-sizing: border-box; }
  html, body {
    width: 1200px;
    height: 1000px;
    overflow: hidden;
    background: var(--page);
  }
  .canvas {
    position: relative;
    width: 1200px;
    height: 1000px;
  }
  .card {
    position: absolute;
    left: 252px;
    top: 152px;
    width: 695px;
    height: 695px;
    background: var(--navy);
    overflow: hidden;
    color: var(--card-text);
  }
  .card-art {
    position: absolute;
    left: 0;
    top: 0;
    width: 695px;
    height: 695px;
  }
  .identity {
    position: absolute;
    left: 36px;
    top: 37px;
  }
  .identity-name {
    font-family: "Outfit", sans-serif;
    font-weight: 800;
    font-size: 41px;
    line-height: 1;
    letter-spacing: 0.4px;
  }
  .identity-role {
    font-family: "Montserrat", sans-serif;
    font-weight: 300;
    font-size: 29px;
    line-height: 1;
    margin-top: 6px;
  }
  .contact {
    position: absolute;
    left: 0;
    width: 695px;
    top: 600px;
    text-align: center;
    font-family: "Montserrat", sans-serif;
    font-style: normal;
    font-weight: 300;
    font-size: 23px;
    line-height: 34px;
    letter-spacing: 0.4px;
  }
  .design-label {
    position: absolute;
    left: 830px;
    top: 872px;
    font-family: "Montserrat", sans-serif;
    font-weight: 400;
    font-size: 44px;
    line-height: 1;
    letter-spacing: 1px;
    color: var(--label-text);
  }
</style>
</head>
<body>
  <main class="canvas">
    <section class="card">
      <svg class="card-art" viewBox="0 0 695 695" role="img" aria-label="Large coral dragonfly illustration spreading its wings across the navy card">
        <defs>
          <linearGradient id="wing-glow" x1="0" y1="0" x2="0" y2="1">
            <stop offset="0" stop-color="#20375a"/>
            <stop offset="0.35" stop-color="#e36d69"/>
            <stop offset="0.62" stop-color="#e36d69"/>
            <stop offset="1" stop-color="#20375a"/>
          </linearGradient>
        </defs>
        <rect x="0" y="120" width="695" height="575" fill="url(#wing-glow)"/>
      </svg>

      <header class="identity">
        <h1 class="identity-name">Theo Last Name</h1>
        <p class="identity-role">CEO &amp; Founder</p>
      </header>

      <address class="contact">
        <p class="contact-phone">P: 720-555-0148</p>
        <p class="contact-email">E: theo@tidalfern.com</p>
      </address>
    </section>

    <p class="design-label">Front 2</p>
  </main>
</body>
</html>
```